Selka Marven Photography Business Card

I need a new business card/ possibly design to use for other marking materials ... I have included my logo below in a few different colors, but can also provide the logo in additional colors and sizes. I would love a card the expresses clean, simple and classy.

Target Market(s)

Portrait photography clients, child photography clients

Industry/Entity Type

Photographer

Contact Information for Business Card

Selka Marven Photography, Fenwick Hollow MA, www.selkamarvenphotography-demo.com
T. 555-203-1946 E. selkamarvenphoto@mailbox-demo.com

Colors
33b8a4
eea4c8
5c5c5c

Requirements
Must have
• I would like to include my logo on card.
Nice to have
• I also like the color brown as well as the choices below. I would like a simple, elegant card, something classy.

```html
<!DOCTYPE html>
<html lang="en">
<head>
<meta charset="utf-8">
<title>Selka Marven Photography – Business Card</title>
<link rel="stylesheet" href="https://fonts.googleapis.com/css2?family=Montserrat:wght@600&family=Oswald:wght@500&family=Open+Sans:wght@400&display=swap">
<style>
  :root {
    --backdrop: #4b4b4d;
    --card-dark: #545456;
    --card-light: #ededee;
    --accent-pink: #e3a2df;
    --silver: #cfcfd1;
    --ink: #3f3f41;
    --ink-soft: #5c5c5c;
  }
  * { box-sizing: border-box; margin: 0; padding: 0; }
  html, body {
    width: 1200px; height: 904px; overflow: hidden;
    background: var(--backdrop);
  }
  .sheet {
    width: 1200px; height: 904px;
    display: flex; flex-direction: column; align-items: center; justify-content: center;
    gap: 36px;
  }
  .card {
    width: 700px; height: 400px; position: relative; overflow: hidden;
    box-shadow: 0 10px 28px rgba(0,0,0,.35);
  }
  .wordmark {
    font-family: "Montserrat", sans-serif; font-weight: 600;
    letter-spacing: 3px; text-transform: uppercase; white-space: nowrap;
  }

  /* Front */
  .card-front { background: var(--card-dark); display: flex; align-items: center; justify-content: center; }
  .card-front .wordmark { color: var(--silver); font-size: 30px; }

  /* Back */
  .card-back { background: var(--card-light); }
  .back-band {
    position: absolute; left: 0; top: 0; width: 100%; height: 178px;
    background: var(--card-dark);
    display: flex; align-items: center; justify-content: center;
  }
  .back-band .wordmark { color: var(--accent-pink); font-size: 24px; }
  .band-rule { position: absolute; left: 0; width: 100%; height: 4px; background: var(--accent-pink); }
  .band-rule.top { top: 188px; }
  .details {
    position: absolute; left: 0; top: 192px; width: 100%; height: 208px;
    padding: 0 28px;
    display: flex; align-items: center; justify-content: center; gap: 22px;
  }
  .studio { text-align: right; white-space: nowrap; }
  .studio-name {
    font-family: "Oswald", sans-serif; font-weight: 500; font-size: 27px;
    color: var(--ink); text-transform: uppercase; letter-spacing: .3px; line-height: 1.15;
  }
  .studio-town { font-family: "Open Sans", sans-serif; font-size: 15px; color: var(--ink-soft); }
  .divider { width: 2px; height: 74px; background: var(--ink); flex: none; }
  .contacts {
    list-style: none; font-family: "Open Sans", sans-serif; font-size: 13px;
    color: var(--ink-soft); white-space: nowrap;
  }
  .contacts li { display: flex; align-items: center; gap: 9px; line-height: 25px; }
  .contacts svg { width: 16px; height: 16px; flex: none; }
</style>
</head>
<body>
<main class="sheet">
  <section class="card card-front" aria-label="Card front">
    <span class="wordmark">Selka Marven Photography</span>
  </section>

  <section class="card card-back" aria-label="Card back">
    <div class="back-band">
      <span class="wordmark">Selka Marven Photography</span>
    </div>
    <div class="band-rule top"></div>
    <div class="details">
      <div class="studio">
        <p class="studio-name">Selka Marven Photography</p>
        <p class="studio-town">Fenwick Hollow MA</p>
      </div>
      <div class="divider"></div>
      <ul class="contacts">
        <li>
          <svg viewBox="0 0 16 16" aria-hidden="true"><circle cx="8" cy="8" r="8" fill="var(--accent-pink)"/><path d="M5.2 4.2l1.5 1.6-.7 1c.6 1.2 1.5 2.1 2.7 2.7l1-.7 1.6 1.5-.9 1.3C7.7 11.4 4.6 8.3 4.4 5.1z" fill="#fff"/></svg>
          555-203-1946
        </li>
        <li>
          <svg viewBox="0 0 16 16" aria-hidden="true"><circle cx="8" cy="8" r="8" fill="var(--accent-pink)"/><rect x="4" y="5.2" width="8" height="5.6" fill="#fff"/><path d="M4 5.2l4 3 4-3" fill="none" stroke="var(--accent-pink)" stroke-width="1"/></svg>
          selkamarvenphoto@mailbox-demo.com
        </li>
        <li>
          <svg viewBox="0 0 16 16" aria-hidden="true"><circle cx="8" cy="8" r="8" fill="var(--accent-pink)"/><circle cx="8" cy="8" r="4" fill="none" stroke="#fff" stroke-width="1.1"/><path d="M4 8h8M8 4c-1.6 2.4-1.6 5.6 0 8M8 4c1.6 2.4 1.6 5.6 0 8" fill="none" stroke="#fff" stroke-width="1"/></svg>
          www.selkamarvenphotography-demo.com
        </li>
      </ul>
    </div>
  </section>
</main>
</body>
</html>
```